Bright Harbor Real Estate Institute

This must be done in word press and I will need about 7 tabs The home page, Information page, Schedule and Cost page which will link to a Email me form, a online registration a about us and location/contact tab Each tab will then open several other pages. The home page will describe different courses that we offer since all the schools are about the same you can get a good ideal by going to qelvanto.org or pinnaclebayrealtyschool.com and looking at their site I would like mine to be similar as the courses are exactly the same but I would like the site to be more modern I also need it to be in word press so I can change it and update the dates as they change I have attached he logo below

Target Market(s)

people interested in getting into real estate and those who need continuing education

Coding

Coded - Design and coding required

Number of Pages Required

5+ page

Font styles to use
Sans Serif

Colors
3276b5

Requirements
Must have
• A page to schedule classes, a tab so the college I am partnering with can link the online courses to the back side, a page that describes the type of classes I offer

```html
<!DOCTYPE html>
<html lang="en">
<head>
<meta charset="utf-8">
<title>Bright Harbor Real Estate Institute</title>
<link href="https://fonts.googleapis.com/css2?family=Roboto:wght@400;500;700&family=Noto+Serif:wght@700&family=Nunito:wght@400;600&display=swap" rel="stylesheet">
<style>
:root{
  --brand:#2c62ad;
  --brand-soft:#3276b5;
  --ink:#2b2b2b;
  --muted:#8a8a8a;
  --dark:#2e2e31;
  --slate:#4b4c52;
  --line:#dcdcdc;
  --white:#ffffff;
}
*{box-sizing:border-box;margin:0;padding:0}
html,body{width:1200px;height:2810px;overflow:hidden;background:var(--white)}
body{position:relative;font-family:'Roboto',sans-serif;color:var(--ink)}
.abs{position:absolute}
.serif{font-family:'Noto Serif',serif;font-weight:700}

/* header */
.brand-mark{left:145px;top:18px;display:flex;align-items:center;gap:12px}
.brand-dot{width:34px;height:34px;border-radius:50%;background:var(--brand)}
.brand-name{font-family:'Roboto',sans-serif;font-weight:700;font-size:19px;line-height:23px;color:var(--brand);width:230px}
.contact{display:flex;align-items:center;gap:14px;top:22px}
.contact .ic{width:40px;height:40px;border:2px solid var(--brand);border-radius:50%;display:flex;align-items:center;justify-content:center}
.contact b{display:block;font-family:'Nunito',sans-serif;font-weight:600;font-size:17px;color:var(--ink)}
.contact span{font-family:'Nunito',sans-serif;font-size:17px;color:var(--ink)}
.phone{left:520px}
.email{left:734px}
.divider{left:711px;top:26px;width:1px;height:40px;background:var(--line)}

/* nav */
.nav{left:0;top:106px;width:1200px;height:42px;background:var(--brand)}
.nav a{position:absolute;top:0;height:42px;line-height:42px;color:var(--white);font-size:13px;font-weight:500;text-decoration:none;letter-spacing:.2px}
.nav .active{left:143px;width:73px;background:var(--slate);text-align:center}

/* hero */
.hero{left:0;top:148px}
.hero-title{left:144px;top:280px;font-size:58px;line-height:69px;color:var(--white);letter-spacing:.5px}
.btn{display:inline-flex;align-items:center;gap:8px;height:48px;padding:0 28px;border-radius:24px;color:var(--white);font-size:15px;font-weight:500}
.hero-btn{left:143px;top:451px;background:var(--brand)}
.arrow-round{width:28px;height:28px;border-radius:50%;background:rgba(0,0,0,.35);border:1px solid rgba(255,255,255,.6);display:flex;align-items:center;justify-content:center}
.dots{left:556px;top:638px;display:flex;gap:7px}
.dots i{width:12px;height:12px;border-radius:50%;background:var(--white)}
.dots i.on{background:transparent;border:2px solid var(--white)}

/* welcome */
.welcome{left:0;width:1200px;text-align:center}
.welcome h2{font-size:46px;color:var(--ink);margin-top:0}
.welcome h3{font-family:'Roboto',sans-serif;font-weight:500;font-size:40px;color:var(--brand);margin-top:12px}

/* features */
.feat h4{font-size:17px;font-weight:500;color:var(--ink);letter-spacing:.2px}
.feat p{font-family:'Nunito',sans-serif;font-size:13.5px;line-height:26px;color:var(--muted);margin-top:14px;width:300px}
.feat .more{display:inline-block;margin-top:14px;padding:0 16px;height:34px;line-height:32px;border:1.5px solid var(--brand);border-radius:17px;color:var(--brand);font-size:13.5px;font-weight:500}
.feat.left{text-align:right}
.diamond{width:110px;height:110px}

/* courses */
.courses{left:0;top:1496px}
.course-title{font-size:30px;line-height:40px;color:var(--white)}
.course-text{font-family:'Nunito',sans-serif;font-size:14.5px;line-height:26px;color:var(--white)}
.price{font-size:32px;font-weight:500;color:var(--white)}
.btn-dark{background:var(--slate)}
.btn-blue{background:var(--brand)}

/* videos */
.vid-title{left:0;width:1200px;top:2055px;text-align:center;font-size:46px}
.card{top:2148px;width:223px;height:267px;border:1px solid var(--line);background:var(--white)}
.card .shot{position:absolute;left:7px;top:7px;width:207px;height:172px}
.card .play{position:absolute;right:12px;top:160px;width:38px;height:38px;border-radius:50%;background:var(--white);border:2px solid var(--brand);display:flex;align-items:center;justify-content:center}
.card h5{position:absolute;left:17px;top:199px;font-size:14px;font-weight:500;color:var(--ink)}
.card p{position:absolute;left:17px;top:222px;width:190px;font-family:'Nunito',sans-serif;font-size:12px;line-height:18px;color:var(--muted)}

/* footer */
.footer{left:0;top:2490px}
.social{left:0;width:1200px;top:2596px;display:flex;justify-content:center;gap:7px}
.social i{width:45px;height:45px;border:2px solid var(--white);border-radius:50%}
.foot-nav{left:0;width:1200px;top:2671px;text-align:center;color:var(--white);font-size:14px;font-weight:500}
.foot-nav span{margin:0 10px}
.foot-info{left:0;width:1200px;top:2711px;text-align:center;color:var(--white);font-family:'Nunito',sans-serif;font-size:14px}
.foot-info em{font-style:normal;margin:0 12px}
.copy{left:0;width:1200px;top:2752px;text-align:center;color:var(--white);font-size:11px}
</style>
</head>
<body>

<!-- header -->
<div class="abs brand-mark"><div class="brand-dot"></div><div class="brand-name">BRIGHT HARBOR REAL ESTATE INSTITUTE</div></div>

<div class="abs contact phone">
  <div class="ic"><svg width="20" height="20" viewBox="0 0 24 24"><path d="M6.6 10.8a15 15 0 0 0 6.6 6.6l2.2-2.2c.3-.3.7-.4 1-.2 1.1.4 2.3.6 3.6.6.6 0 1 .4 1 1V20c0 .6-.4 1-1 1A17 17 0 0 1 3 4c0-.6.4-1 1-1h3.5c.6 0 1 .4 1 1 0 1.3.2 2.5.6 3.6.1.3 0 .7-.2 1z" fill="var(--brand)"/></svg></div>
  <div><b>Phone</b><span>1 888 888 8888</span></div>
</div>
<div class="abs divider"></div>
<div class="abs contact email">
  <div class="ic" style="background:var(--white)"><svg width="20" height="16" viewBox="0 0 20 16"><rect x="0" y="0" width="20" height="16" rx="2" fill="var(--brand)"/><path d="M1 2l9 7 9-7" stroke="#fff" stroke-width="1.6" fill="none"/></svg></div>
  <div><b>Email Us</b><span>info@brightharborinstitute.com</span></div>
</div>

<!-- nav -->
<nav class="abs nav">
  <a class="active">HOME</a>
  <a style="left:235px">INFORMATION</a>
  <a style="left:360px">SCHEDULE &amp; COST</a>
  <a style="left:512px">REGISTRATION</a>
  <a style="left:640px">ONLINE COURSE</a>
  <a style="left:778px">ADVANTAGE</a>
  <a style="left:889px">CONTACT</a>
  <svg class="abs" style="left:982px;top:14px" width="14" height="14" viewBox="0 0 14 14"><circle cx="6" cy="6" r="4.5" stroke="#fff" stroke-width="2" fill="none"/><path d="M9.5 9.5L13 13" stroke="#fff" stroke-width="2"/></svg>
  <svg class="abs" style="left:1030px;top:10px" width="24" height="22" viewBox="0 0 24 22"><path d="M1 3h4l3 11h11l3-8H7" stroke="#fff" stroke-width="1.6" fill="none"/><circle cx="10" cy="18" r="1.7" fill="#fff"/><circle cx="17" cy="18" r="1.7" fill="#fff"/><circle cx="19" cy="4" r="3.5" fill="var(--brand)" stroke="#fff"/></svg>
</nav>

<!-- hero -->
<svg class="abs hero" width="1200" height="620" viewBox="0 0 1200 620" role="img" aria-label="Photo of a smiling student with glasses working on a laptop outdoors on sunny grass">
  <defs>
    <linearGradient id="heroFill" x1="0" y1="0" x2="1" y2="1">
      <stop offset="0" stop-color="#6f7d3a"/>
      <stop offset=".45" stop-color="#b48a4a"/>
      <stop offset=".75" stop-color="#8a7050"/>
      <stop offset="1" stop-color="#4f5a2c"/>
    </linearGradient>
  </defs>
  <path d="M0 0H1200V430Q640 640 0 430Z" fill="url(#heroFill)"/>
  <path d="M0 430Q560 640 880 545" stroke="var(--brand)" stroke-width="9" fill="none"/>
  <path d="M20 445Q560 655 860 560" stroke="var(--brand)" stroke-width="2" fill="none"/>
  <path d="M880 545Q1060 490 1200 430" stroke="var(--slate)" stroke-width="12" fill="none"/>
</svg>
<div class="abs hero-title serif">ALL-ROUND REAL<br>ESTATE LEARNING</div>
<div class="abs btn hero-btn">GET STARTED <svg width="14" height="14" viewBox="0 0 14 14"><circle cx="7" cy="7" r="7" fill="#fff"/><path d="M5 4l3 3-3 3" stroke="var(--brand)" stroke-width="2" fill="none"/></svg></div>
<div class="abs arrow-round" style="left:73px;top:382px;width:32px;height:32px"><svg width="10" height="12" viewBox="0 0 10 12"><path d="M7 1L2 6l5 5" stroke="#fff" stroke-width="2" fill="none"/></svg></div>
<div class="abs arrow-round" style="left:1096px;top:382px;width:32px;height:32px"><svg width="10" height="12" viewBox="0 0 10 12"><path d="M3 1l5 5-5 5" stroke="#fff" stroke-width="2" fill="none"/></svg></div>
<div class="abs dots"><i></i><i></i><i class="on"></i><i></i><i></i></div>

<!-- welcome -->
<div class="abs welcome" style="top:818px">
  <h2 class="serif">WELCOME TO</h2>
  <h3>Bright Harbor Real Estate Institute</h3>
</div>

<!-- features -->
<div class="abs feat left" style="left:144px;top:1020px">
  <h4>INFORMATION</h4>
  <p>Lorem ipsum dolor sit amet, consectetur adipiscing elit, sed do eiusmod tempor incididune magna aliquependiss ultrices gravida.</p>
  <span class="more">READ MORE</span>
</div>
<div class="abs feat" style="left:756px;top:1020px">
  <h4>SCHEDULE &amp; COST</h4>
  <p>Lorem ipsum dolor sit amet, consectetur adipiscing elit, sed do eiusmod tempor incididune magna aliquependiss ultrices gravida.</p>
  <span class="more">READ MORE</span>
</div>
<div class="abs feat left" style="left:144px;top:1246px">
  <h4>ONLINE COURSES</h4>
  <p>Lorem ipsum dolor sit amet, consectetur adipiscing elit, sed do eiusmod tempor incididune magna aliquependiss ultrices gravida.</p>
  <span class="more">READ MORE</span>
</div>
<div class="abs feat" style="left:756px;top:1246px">
  <h4>REGISTRATION</h4>
  <p>Lorem ipsum dolor sit amet, consectetur adipiscing elit, sed do eiusmod tempor incididune magna aliquependiss ultrices gravida.</p>
  <span class="more">READ MORE</span>
</div>

<svg class="abs diamond" style="left:465px;top:1020px" viewBox="0 0 110 110"><path d="M55 2L108 55 55 108 2 55Z" fill="#fff" stroke="var(--slate)" stroke-width="2"/><circle cx="55" cy="55" r="18" fill="var(--brand)"/><circle cx="55" cy="46" r="3" fill="#fff"/><rect x="52" y="52" width="6" height="15" fill="#fff"/></svg>
<svg class="abs diamond" style="left:629px;top:1020px" viewBox="0 0 110 110"><path d="M55 2L108 55 55 108 2 55Z" fill="#fff" stroke="var(--brand)" stroke-width="2"/><rect x="39" y="42" width="32" height="28" rx="2" fill="none" stroke="var(--slate)" stroke-width="3"/><rect x="39" y="42" width="32" height="8" fill="var(--slate)"/><rect x="45" y="36" width="3" height="9" fill="var(--slate)"/><rect x="62" y="36" width="3" height="9" fill="var(--slate)"/></svg>
<svg class="abs diamond" style="left:465px;top:1245px" viewBox="0 0 110 110"><path d="M55 2L108 55 55 108 2 55Z" fill="#fff" stroke="var(--brand)" stroke-width="2"/><rect x="35" y="40" width="40" height="27" rx="2" fill="var(--slate)"/><rect x="39" y="44" width="32" height="18" fill="#fff"/><rect x="50" y="67" width="10" height="5" fill="var(--slate)"/><rect x="44" y="72" width="22" height="3" fill="var(--slate)"/></svg>
<svg class="abs diamond" style="left:629px;top:1245px" viewBox="0 0 110 110"><path d="M55 2L108 55 55 108 2 55Z" fill="#fff" stroke="var(--slate)" stroke-width="2"/><rect x="36" y="44" width="28" height="28" rx="5" fill="none" stroke="var(--brand)" stroke-width="3"/><path d="M50 62l18-18 5 5-18 18-7 2z" fill="var(--brand)"/></svg>

<!-- courses -->
<svg class="abs courses" width="1200" height="487" viewBox="0 0 1200 487">
  <defs>
    <linearGradient id="leftFill" x1="0" y1="0" x2="1" y2="1"><stop offset="0" stop-color="#3a6db5"/><stop offset="1" stop-color="#2a5aa3"/></linearGradient>
    <linearGradient id="rightFill" x1="0" y1="0" x2="1" y2="1"><stop offset="0" stop-color="#5a5b61"/><stop offset="1" stop-color="#3f4046"/></linearGradient>
  </defs>
  <rect width="1200" height="487" fill="url(#rightFill)" role="img" aria-label="Photo of a student reading an open book"/>
  <path d="M0 0H551L606 215 547 487H0Z" fill="url(#leftFill)" role="img" aria-label="Photo of a smiling student at a laptop, tinted blue"/>
  <path d="M561 0L618 215 557 487" stroke="#fff" stroke-width="3" fill="none"/>
  <path d="M578 80L627 215 586 380" stroke="#fff" stroke-width="2" fill="none"/>
</svg>
<div class="abs course-title serif" style="left:144px;top:1586px">THE TENNESSEE REAL<br>ESTATE PRINCIPLES<br>COURSE</div>
<div class="abs course-text" style="left:144px;top:1723px">Sed ut perspiciatis unde omnis iste natus error sit voluptatem</div>
<div class="abs price" style="left:143px;top:1764px">$360.00</div>
<div class="abs btn btn-dark" style="left:144px;top:1834px">VIEW COURSE <svg width="14" height="14" viewBox="0 0 14 14"><circle cx="7" cy="7" r="7" fill="#fff"/><path d="M5 4l3 3-3 3" stroke="var(--slate)" stroke-width="2" fill="none"/></svg></div>

<div class="abs course-title serif" style="right:143px;top:1586px;text-align:right">THE COURSE FOR NEW<br>AFFILIATES COURSE</div>
<div class="abs course-text" style="right:143px;top:1684px;text-align:right;width:420px">Sed ut perspiciatis unde omnis iste natus error sit voluptatem ccusantium doloremque laudantium</div>
<div class="abs price" style="right:143px;top:1764px">$165.00</div>
<div class="abs btn btn-blue" style="right:143px;top:1834px">VIEW COURSE <svg width="14" height="14" viewBox="0 0 14 14"><circle cx="7" cy="7" r="7" fill="#fff"/><path d="M5 4l3 3-3 3" stroke="var(--brand)" stroke-width="2" fill="none"/></svg></div>

<!-- videos -->
<div class="abs vid-title serif">LATEST VIDEOS</div>

<div class="abs card" style="left:132px">
  <div class="shot" role="img" aria-label="Photo of a student writing notes beside a laptop" style="background:linear-gradient(135deg,#e9e3dc,#b9a999)"></div>
  <div class="play"><svg width="14" height="16" viewBox="0 0 14 16"><path d="M1 1l12 7-12 7z" fill="var(--brand)"/></svg></div>
  <h5>CUM SOLUTA</h5><p>Itaque earum rerum hic tenetura sapiente delectus,</p>
</div>
<div class="abs card" style="left:370px">
  <div class="shot" role="img" aria-label="Photo of a student on a sofa with a laptop" style="background:linear-gradient(135deg,#6d6a72,#3d4050)"></div>
  <div class="play"><svg width="14" height="16" viewBox="0 0 14 16"><path d="M1 1l12 7-12 7z" fill="var(--brand)"/></svg></div>
  <h5>PRAESENTIUM</h5><p>Itaque earum rerum hic tenetura sapiente delectus,</p>
</div>
<div class="abs card" style="left:608px">
  <div class="shot" role="img" aria-label="Overhead photo of a person with a laptop on an armchair beside a small table" style="background:linear-gradient(135deg,#cbbba5,#6b5f55)"></div>
  <div class="play"><svg width="14" height="16" viewBox="0 0 14 16"><path d="M1 1l12 7-12 7z" fill="var(--brand)"/></svg></div>
  <h5>VOLUPTATUM</h5><p>Itaque earum rerum hic tenetura sapiente delectus,</p>
</div>
<div class="abs card" style="left:845px">
  <div class="shot" role="img" aria-label="Photo of hands typing on a laptop at a bright desk" style="background:linear-gradient(135deg,#e7ecef,#9aa6b1)"></div>
  <div class="play"><svg width="14" height="16" viewBox="0 0 14 16"><path d="M1 1l12 7-12 7z" fill="var(--brand)"/></svg></div>
  <h5>QUOS DOLORES</h5><p>Itaque earum rerum hic tenetura sapiente delectus,</p>
</div>

<!-- footer -->
<svg class="abs footer" width="1200" height="320" viewBox="0 0 1200 320">
  <path d="M0 180Q600 -60 1200 180V320H0Z" fill="var(--dark)"/>
  <path d="M0 170Q600 -75 1200 180" stroke="var(--slate)" stroke-width="12" fill="none"/>
  <path d="M360 52Q780 -20 1200 170" stroke="var(--brand)" stroke-width="8" fill="none"/>
  <path d="M380 45Q790 -32 1200 158" stroke="var(--brand)" stroke-width="2" fill="none"/>
</svg>
<div class="abs social"><i></i><i></i><i></i><i></i><i></i></div>
<div class="abs foot-nav">HOME<span>/</span>INFORMATION<span>/</span>SCHEDULE &amp; COST<span>/</span>REGISTRATION<span>/</span>ONLINE COURSE<span>/</span>ADVANTAGE<span>/</span>CONTACT</div>
<div class="abs foot-info">Ut enim ad minima veniam<em>|</em>1 888 888 8888<em>|</em>hello@brightharborinstitute.com</div>
<div class="abs copy">Copyright 2019 Bright Harbor Real Estate Institute. All Rights Reserved &nbsp;|&nbsp; Terms of Use</div>

</body>
</html>
```